Plumbing Website

Design a simple 4 page website based on our provided logo and sketches. Winning designer should be willing to upgrade as needed (for additional fee). A design that includes SEO features is a plus.
I would like to see Home, , Services, Recent Jobs (set up for pictures), Contact. I like the water dropplet back ground. Please dont put logo in a box. File attached as exaple only, I am looking for a request service now button in the middle that will have a form fill to be emailed to two different addresses,
I would like to see vibrant colors. Examples of sites I like are www.maplewickplumbingandheat.com look also at www.kfv-fernvalleyplumbing.com - this site is too busy but has good seo features.

```html
<!DOCTYPE html>
<html lang="en">
<head>
<meta charset="utf-8">
<title>Canyon Crest Plumbing – Services</title>
<meta name="description" content="Canyon Crest Plumbing serves Maple Ridge and Cedar Falls with residential, commercial and industrial plumbing.">
<link rel="stylesheet" href="https://fonts.googleapis.com/css2?family=Source+Sans+3:wght@300;400;700&display=swap">
<style>
  :root {
    --brand-blue: #1c5cf5;
    --navy: #0b2a86;
    --footer-navy: #0a1f5e;
    --active-yellow: #e8c80c;
    --emergency-red: #e3141c;
    --text-grey: #4a4a4a;
    --white: #ffffff;
  }
  * { box-sizing: border-box; margin: 0; padding: 0; }
  html, body { width: 920px; height: 1200px; overflow: hidden; background: var(--white); }
  body { font-family: "Source Sans 3", sans-serif; color: var(--text-grey); position: relative; }

  .site-header { position: relative; height: 108px; }
  .brand { position: absolute; left: 42px; top: 12px; color: var(--brand-blue); font-weight: 700; font-size: 27px; line-height: 28px; letter-spacing: 0.5px; text-transform: uppercase; }
  .emergency-button {
    position: absolute; left: 420px; top: 10px; width: 80px; height: 80px; border-radius: 50%;
    background: var(--emergency-red); border: 2px solid #b80d14; color: var(--white);
    display: flex; flex-direction: column; align-items: center; justify-content: center;
    text-align: center; font-weight: 700; line-height: 1.05; text-decoration: none;
  }
  .emergency-button .label { font-size: 11px; }
  .emergency-button .press { font-size: 9px; margin: 3px 0; }
  .header-contact { position: absolute; right: 64px; top: 12px; text-align: right; color: var(--navy); }
  .header-contact .area { font-weight: 700; font-size: 16px; letter-spacing: -0.3px; padding-right: 32px; }
  .header-contact .phone { font-weight: 700; font-size: 38px; line-height: 44px; letter-spacing: 0.3px; }

  .main-nav { position: absolute; left: 42px; top: 108px; width: 836px; height: 37px; background: var(--brand-blue); display: flex; }
  .main-nav a { color: var(--white); text-decoration: none; font-weight: 700; font-size: 17px; display: flex; align-items: center; justify-content: center; border-right: 2px solid #6f97fb; }
  .main-nav a.active { background: var(--active-yellow); color: var(--navy); border: 1px solid #b89d06; }
  .main-nav a:nth-child(1) { width: 109px; }
  .main-nav a:nth-child(2) { width: 136px; }
  .main-nav a:nth-child(3) { width: 165px; }
  .main-nav a:nth-child(4) { width: 136px; }

  .service-list { position: absolute; top: 205px; left: 42px; width: 836px; display: flex; list-style: none; }
  .service-column { list-style: none; width: 428px; }
  .service-column li { font-weight: 300; font-size: 20.5px; line-height: 34px; color: var(--text-grey); }

  .tagline { position: absolute; top: 1010px; left: 0; width: 920px; text-align: center; color: var(--navy); font-weight: 700; font-size: 29px; }

  .site-footer { position: absolute; top: 1057px; left: 0; width: 920px; height: 100px; background: var(--brand-blue); color: var(--white); }
  .footer-nav { position: absolute; left: 42px; top: 16px; font-weight: 300; font-size: 15px; }
  .footer-nav a { color: var(--white); text-decoration: none; }
  .footer-nav .sep { margin: 0 10px; }
  .footer-contact { position: absolute; right: 42px; top: 16px; text-align: right; }
  .footer-contact .area { font-weight: 400; font-size: 16px; }
  .footer-contact .phone { font-weight: 700; font-size: 37px; line-height: 46px; }
  .copyright { position: absolute; top: 1157px; left: 0; width: 920px; height: 43px; background: var(--footer-navy); color: #c9d2ec; font-weight: 300; font-size: 13px; display: flex; align-items: center; justify-content: center; }
</style>
</head>
<body>
  <header class="site-header">
    <div class="brand">Canyon Crest<br>Plumbing</div>
    <a class="emergency-button" href="#contact">
      <span class="label">Plumbing</span>
      <span class="press">Press here</span>
      <span class="label">Emergency</span>
    </a>
    <div class="header-contact">
      <div class="area">MAPLE RIDGE / CEDAR FALLS</div>
      <div class="phone">951-555-0184</div>
    </div>
  </header>

  <nav class="main-nav">
    <a class="active" href="#home">HOME</a>
    <a href="#services">SERVICES</a>
    <a href="#recent-jobs">RECENT JOBS</a>
    <a href="#contact">CONTACT</a>
  </nav>

  <main>
    <div class="service-list">
      <ul class="service-column">
        <li>Backflow Preventers / Backflow Testing</li>
        <li>Catch Basins</li>
        <li>Ceiling Leaks / Leaks thru the ceiling</li>
        <li>Circulator Pumps / Water Heater Pumps</li>
        <li>Clogged Drains / Sewer Back Ups</li>
        <li>Commercial</li>
        <li>Copper Piping / PEX re-piping</li>
        <li>Drain Cleaning</li>
        <li>Electric Water Heaters</li>
        <li>Encroachment Permits</li>
        <li>Excavation</li>
        <li>Faucets Leaking / Dripping Fixtures</li>
        <li>Fire Hydrants</li>
        <li>Fire Line</li>
        <li>Garbage Disposals</li>
        <li>Gas Lines</li>
        <li>Grease Traps</li>
        <li>HOA water systems</li>
        <li>Hot taps</li>
        <li>Hydro Jetting Service</li>
        <li>Industrial</li>
        <li>Leak Detection</li>
      </ul>
      <ul class="service-column">
        <li>Line Locating</li>
        <li>Low Flow Toilets / Green Products</li>
        <li>Odor Issues / Smoke testing</li>
        <li>Pipe Location / Line Tracing</li>
        <li>Pressure Relief Valves / Pressure Regulators</li>
        <li>Pumps</li>
        <li>Residential</li>
        <li>Roof Drains / Area Drains</li>
        <li>Septic Tanks</li>
        <li>Sewer Back-ups</li>
        <li>Shower Heads</li>
        <li>Sinks Leaking</li>
        <li>Sump Pumps</li>
        <li>Tank less Hot Water Heaters</li>
        <li>Tenant improvements</li>
        <li>Toilets Leaking</li>
        <li>Trenchless Technology</li>
        <li>Urinals</li>
        <li>Video Camera Inspection</li>
        <li>Water Heaters</li>
        <li>Water Pressure Issues</li>
      </ul>
    </div>
    <p class="tagline">We are looking forward to hearing from you!</p>
  </main>

  <footer class="site-footer">
    <nav class="footer-nav">
      <a href="#home">HOME</a><span class="sep">/</span><a href="#services">SERVICES</a><span class="sep">/</span><a href="#recent-jobs">RECENT JOBS</a><span class="sep">/</span><a href="#contact">CONTACT</a>
    </nav>
    <div class="footer-contact">
      <div class="area">MAPLE RIDGE / CEDAR FALLS</div>
      <div class="phone">951-555-0184</div>
    </div>
  </footer>
  <div class="copyright">Copyright © 2013 Canyon Crest Plumbing</div>
</body>
</html>
```